依頼詳細
産後骨盤矯正をメインにしているので、小さい子供のいる女性が好むような看板にしたいと思っています。
また、目立つ看板で分かりやすいというのも重視しているため、看板の文字は『全身もみほぐし 整体』と大きく目立たせ、
店名は『凪』、もしくは『Nagi』で、書かれていれば良い程度に考えています。
そのため、看板の内容が固い印象になると思いますので、書体や色合い、看板自体の形、ロゴ等遊び心を入れて可愛いデザインにしたいと考えています。
外壁の色と形が少し特殊なため、それを活かした看板になると良いと思っています。
記載項目
2階部分の窓から下に可能な限り大きく付けたいと思っています。
しかし、細長くなりすぎてしまうように感じるので、何か良いアイディアはないかと検討中です。
写真添付致しますので、ご確認頂けると幸いです。
希望イメージ
シンプル 複雑
単色 カラフル
暗い 明るい
日常 高級
遊び心 厳粛
未来的 伝統的
女性的 男性的
希望する色
黄・オレンジ系、緑系、茶系
補足説明
今回は看板デザインの募集です。
その為、ロゴデザインのご提案は不要です。
普段看板ではあまり使われていないような、少し変わった書体で作れたら面白いかなと思っています。
書体の珍しさで目立たせ、さらに可愛い仕上がりの看板になれば1番良いかなと思っています。
宜しくお願い致します。
『全身もみほぐし 整体』 → 『全身もみほぐし 全身矯正』 に変更をお願い致します。
どうしても入らない場合には、『全身もみほぐし 矯正』 に変更お願い致します。

また、サブタイトルのように入れられるようであれば、『産後骨盤矯正、足つぼ、整体、肩こり・腰痛』というワードを入れたいと思ってます。
入れたい順位は、1.産後骨盤矯正 2.足つぼ〜で、手前から順に入れても見た目がおかしくないだけのワードを入れるというイメージです。

宜しくお願い致します。
■ 選んだ理由

この度は、素敵なデザインをありがとうございました。
可愛いらしさ、目立つこと、何の店か一目でわかるという私の希望が全て叶った看板に巡り会えました。
やりとりも迅速、丁寧で助かりました。
本当にありがとうございます。

■ 提案者全員のお礼・コメント

この度は沢山のご提案をありがとうございました。
最後まで悩むデザインもあり、本当に皆様には良きご提案を頂き感謝しかありません。
今回、初めてジョブラを利用させて頂きましたが、今後も機会があればこちらを利用したいと思います。
皆様、本当にありがとうございました。

```html
<!DOCTYPE html>
<html lang="ja">
<head>
<meta charset="utf-8">
<title>全身もみほぐし 整体 看板デザイン</title>
<link rel="stylesheet" href="https://fonts.googleapis.com/css2?family=M+PLUS+Rounded+1c:wght@800&family=Noto+Sans+JP:wght@400&display=swap">
<style>
  :root {
    --paper: #ffffff;
    --ink: #111111;
    --wood-light: #f3dcb4;
    --wood-mid: #e8c48e;
    --wood-dark: #d9ad72;
    --disc-outer: #6b3a1c;
    --disc-inner: #8a5228;
    --letter: #f07a12;
    --letter-edge: #ffffff;
    --plaque: #e9f3c4;
    --plaque-edge: #7aa83a;
    --name: #3fa42c;
  }
  html, body {
    margin: 0;
    padding: 0;
    overflow: hidden;
    background: var(--paper);
  }
  .sheet {
    position: relative;
    width: 1200px;
    height: 849px;
    background: var(--paper);
    overflow: hidden;
  }
  .sheet svg { display: block; }
  .sign-letter {
    font-family: "M PLUS Rounded 1c", sans-serif;
    font-weight: 800;
    font-size: 48px;
    fill: var(--letter);
    stroke: var(--letter-edge);
    stroke-width: 6px;
    stroke-linejoin: round;
    paint-order: stroke fill;
    text-anchor: middle;
    dominant-baseline: central;
  }
  .shop-name {
    font-family: "M PLUS Rounded 1c", sans-serif;
    font-weight: 800;
    font-size: 32px;
    fill: var(--name);
    text-anchor: middle;
    dominant-baseline: central;
  }
  .disc { fill: var(--disc-outer); }
  .disc-face { fill: var(--disc-inner); }
  .plaque { fill: var(--plaque); stroke: var(--plaque-edge); stroke-width: 4; }
  .title-block rect { fill: none; stroke: var(--ink); stroke-width: 1.2; }
  .title-block .brand-cell { fill: var(--ink); }
  .field-label {
    font-family: "Noto Sans JP", sans-serif;
    font-size: 10px;
    fill: var(--ink);
  }
</style>
</head>
<body>
<div class="sheet">
  <svg width="1200" height="849" viewBox="0 0 1200 849" xmlns="http://www.w3.org/2000/svg">
    <defs>
      <linearGradient id="woodTone" x1="0" y1="0" x2="1" y2="0">
        <stop offset="0" stop-color="var(--wood-mid)"/>
        <stop offset="0.3" stop-color="var(--wood-light)"/>
        <stop offset="0.6" stop-color="var(--wood-mid)"/>
        <stop offset="1" stop-color="var(--wood-light)"/>
      </linearGradient>
    </defs>

    <!-- sheet rules -->
    <rect class="rule-top-thick" x="20" y="30" width="1160" height="9" fill="var(--ink)"/>
    <rect class="rule-top-thin" x="20" y="43" width="1160" height="3" fill="var(--ink)"/>
    <rect class="rule-bottom" x="20" y="819" width="1160" height="9" fill="var(--ink)"/>

    <!-- signboard -->
    <g class="signboard">
      <rect x="58" y="336" width="1082" height="160" fill="url(#woodTone)" role="img" aria-label="明るい木目の板の背景"/>
      <path class="cutout" d="M114 497 C250 428 500 408 744 497 Z" fill="var(--paper)"/>
      <path class="cutout" d="M840 497 C880 430 1040 430 1074 497 Z" fill="var(--paper)"/>

      <g class="letter-discs">
        <g><circle class="disc" cx="138" cy="426" r="44"/><circle class="disc-face" cx="138" cy="426" r="36"/><text class="sign-letter" x="138" y="426">全</text></g>
        <g><circle class="disc" cx="226" cy="396" r="44"/><circle class="disc-face" cx="226" cy="396" r="36"/><text class="sign-letter" x="226" y="396">身</text></g>
        <g><circle class="disc" cx="314" cy="390" r="44"/><circle class="disc-face" cx="314" cy="390" r="36"/><text class="sign-letter" x="314" y="390">も</text></g>
        <g><circle class="disc" cx="406" cy="390" r="44"/><circle class="disc-face" cx="406" cy="390" r="36"/><text class="sign-letter" x="406" y="390">み</text></g>
        <g><circle class="disc" cx="494" cy="396" r="44"/><circle class="disc-face" cx="494" cy="396" r="36"/><text class="sign-letter" x="494" y="396">ほ</text></g>
        <g><circle class="disc" cx="582" cy="402" r="44"/><circle class="disc-face" cx="582" cy="402" r="36"/><text class="sign-letter" x="582" y="402">ぐ</text></g>
        <g><circle class="disc" cx="672" cy="426" r="44"/><circle class="disc-face" cx="672" cy="426" r="36"/><text class="sign-letter" x="672" y="426">し</text></g>
        <g><circle class="disc" cx="832" cy="420" r="44"/><circle class="disc-face" cx="832" cy="420" r="36"/><text class="sign-letter" x="832" y="420">整</text></g>
        <g><circle class="disc" cx="920" cy="390" r="44"/><circle class="disc-face" cx="920" cy="390" r="36"/><text class="sign-letter" x="920" y="390">体</text></g>
      </g>

      <g class="name-plaque">
        <ellipse class="plaque" cx="1054" cy="396" rx="72" ry="27"/>
        <text class="shop-name" x="1054" y="396">Nagi</text>
      </g>
    </g>

    <!-- title block -->
    <g class="title-block">
      <rect class="brand-cell" x="196" y="762" width="132" height="40"/>
      <rect x="328" y="762" width="157" height="40"/>
      <rect x="485" y="762" width="342" height="40"/>
      <rect x="827" y="762" width="176" height="40"/>
      <text class="field-label" x="335" y="775">Date</text>
      <text class="field-label" x="492" y="775">Customer Name</text>
      <text class="field-label" x="834" y="775">Designer</text>
    </g>
  </svg>
</div>
</body>
</html>
```